Small rum distillery looking for bottle design

Small rum distillery in Estonia. Looking for bottle lable design. It should be simple but at the same time point out from the variety of other bottles.
As we are a small nordic country, design can be some how nordic or represent our country. It can also have some connection with sailing or sea as we know it pirates love it.
Bottle we are using is Corvane 540

Industry/Entity Type

food and beverage

Other font styles liked:
• Baskerville

```html
<!DOCTYPE html>
<html lang="en">
<head>
<meta charset="UTF-8">
<title>Halvik Distillery – White Rum Label</title>
<link rel="stylesheet" href="https://fonts.googleapis.com/css2?family=Libre+Baskerville:wght@400;700&family=Pinyon+Script&display=swap">
<style>
  :root {
    --page: #ffffff;
    --label-charcoal: #3b3b3d;
    --pattern-tone: #4a4a4d;
    --gold: #c4952e;
    --ink-light: #f2f2f2;
    --rule: rgba(255, 255, 255, 0.45);
  }
  html, body {
    margin: 0;
    padding: 0;
    width: 1200px;
    height: 900px;
    overflow: hidden;
    background: var(--page);
  }
  .canvas {
    position: relative;
    width: 1200px;
    height: 900px;
  }
  .rum-label {
    position: absolute;
    left: 150px;
    top: 56px;
    width: 900px;
    height: 787.5px;
  }
  .serif { font-family: "Libre Baskerville", Baskerville, serif; }
  .script { font-family: "Pinyon Script", cursive; }
  .label-body { fill: var(--label-charcoal); }
  .gold-fill { fill: var(--gold); }
  .gold-stroke { stroke: var(--gold); }
  .pattern-zone { fill: var(--pattern-tone); }
  .rule-line { stroke: var(--rule); stroke-width: 0.8; }
  .text-gold { fill: var(--gold); }
  .text-light { fill: var(--ink-light); }
</style>
</head>
<body>
<main class="canvas">
  <svg class="rum-label" viewBox="0 0 480 420" xmlns="http://www.w3.org/2000/svg" aria-label="Halvik Distillery White Rum label">
    <!-- label base -->
    <rect class="label-body" x="0" y="18" width="480" height="400"/>
    <rect class="gold-fill top-band" x="0" y="18" width="480" height="5"/>
    <rect class="gold-fill bottom-band" x="0" y="401" width="480" height="17"/>

    <!-- crest tab -->
    <circle class="label-body crest-tab" cx="240" cy="46" r="46"/>
    <rect class="gold-fill crest-rule" x="0" y="53" width="196" height="2"/>
    <rect class="gold-fill crest-rule" x="284" y="53" width="196" height="2"/>
    <circle class="brand-mark" cx="240" cy="42" r="17" fill="none" stroke="var(--ink-light)" stroke-width="1.4"/>

    <!-- corner geometric patterns -->
    <g role="img" aria-label="Geometric art deco line pattern in the label corners">
      <polygon class="pattern-zone" points="0,58 125,58 0,178"/>
      <polygon class="pattern-zone" points="480,58 355,58 480,178"/>
      <polygon class="pattern-zone" points="0,282 0,401 118,401"/>
      <polygon class="pattern-zone" points="480,282 480,401 362,401"/>
    </g>

    <!-- brand name -->
    <text class="serif text-gold brand-name" x="240" y="116" font-size="27" text-anchor="middle" letter-spacing="1">HALVIK</text>
    <line class="gold-stroke" x1="178" y1="124" x2="302" y2="124" stroke-width="0.8"/>
    <text class="serif text-gold brand-sub" x="240" y="139" font-size="8.5" text-anchor="middle" letter-spacing="3">DISTILLERY</text>

    <!-- product title -->
    <text class="script text-light tagline" x="240" y="195" font-size="21" text-anchor="middle">Finest Estonian</text>
    <text class="script text-light est" x="143" y="243" font-size="12" text-anchor="middle">Est.</text>
    <text class="serif text-gold product-name" x="240" y="263" font-size="58" text-anchor="middle">RUM</text>
    <text class="script text-light est-year" x="338" y="243" font-size="12" text-anchor="middle">2023</text>
    <line class="rule-line" x1="148" y1="271" x2="332" y2="271"/>
    <text class="serif text-light variant" x="240" y="292" font-size="17" text-anchor="middle">WHITE</text>
    <line class="rule-line" x1="170" y1="299" x2="310" y2="299"/>

    <!-- details -->
    <text class="serif text-light detail" x="240" y="331" font-size="8" text-anchor="middle">DISTILLED AND HANDCRAFTED</text>
    <text class="serif text-light detail" x="240" y="341" font-size="8" text-anchor="middle">BY PROFESSIONAL</text>
    <text class="serif text-light origin" x="240" y="358" font-size="11" text-anchor="middle">PRODUCT OF ESTONIA</text>
    <line class="rule-line" x1="158" y1="366" x2="322" y2="366"/>
    <text class="serif text-light spec" x="216" y="384" font-size="11" text-anchor="end">43% alc</text>
    <g class="spec-divider" stroke="var(--ink-light)" fill="none" stroke-width="0.9">
      <circle cx="240" cy="380" r="3.5"/>
      <line x1="240" y1="374" x2="240" y2="386"/>
    </g>
    <text class="serif text-light spec" x="256" y="384" font-size="11" text-anchor="start">750ml</text>
    <line class="rule-line" x1="158" y1="395" x2="322" y2="395"/>
  </svg>
</main>
</body>
</html>
```